Inspiring book cover design (business book for designers and innovators)

I'm writing my first book, to be published early next year. I'm struggling to come up with an inspiring book cover design. I need your help!

Information to be included on the cover:
Book Title: Bright maker's manual
Subtitle: Designing products and services that make sense
Author: Marieke Vollen
Optional (not sure yet if I should include this on the cover): with online toolset

The book will be a square, size 170 x 170 mm
In the uploaded file you can find some example pages from the inside of the book. The cover design should fit with the design style of the example pages. The cover should "jump out" from the shelve in a bookstore and should attract designers, innovators, product managers, developers, and startup founders to buy the book.
Publisher: www.quarlomedia.example

About the book:
Why do some products fail while others become a success? Why do so many companies launch crappy products and services that nobody wants? This book is both a guide to and a source of inspiration for, designing products and services that make sense. Because if they make sense to people, people will want them.
In order for tech products and services to make sense, and create value for users, we need to apply technologies in a meaningful way. We can achieve this by designing strong benefits and at the same time minimizing resistance users might have against new technologies.
This book offers a complete overview of how to develop products and services that make sense: 27 ways to strengthen benefits and 28 ways to mitigate resistance. It offers practical insights, examples, tips, and tools to design products and services that people will love to use.

About the author:
https://www.profilehub.example/in/mariekevollen/

Target Market(s)

designers, innovators, product managers, developers, and startup founders

Industry/Entity Type

Design Agency

Font styles to use
Other font styles liked:
• You can choose. The inside of the book uses 3 fonts: LuloCleanW01-OneBold, Sansation, Segoe UI

Requirements
Must have
• Clean, yet creative design.
Square shape
Fits the design style of the example pages
Sans serif fonts. Do not have to be the same fonts like the ones that are used inside the book (LuloCleanW01-OneBold, Sansation, Segoe UI), but should go well with them.

Bright makers manual
55 ways to build products and services people want
Marieke Vollen
Nice to have
• I have several ideas that you might take as a starting point:
1) Do something with the left brain (rational, more digital) - right brain (creative, more emotional). For products to make sense, it needs to appeal to both parts of the brain
2) Work with a pattern, for example a (polygonal) triangular pattern
3) playful element in the letters, for example turning the O in innovator's into an on-off button or a stylish smiley, flipping the N in innovator's, doing something playful with the ' in innovator's
I've uploaded some images as a source of inspiration.

The cover should have a different color than the red/blue used in the example pages, but should fit the color palette that is used in the example pages.
Trigger curiosity.
Should not have
• Photographic pictures

```html
<!DOCTYPE html>
<html lang="en">
<head>
<meta charset="utf-8">
<title>Bright makers manual — cover</title>
<link rel="stylesheet" href="https://fonts.googleapis.com/css2?family=Montserrat:wght@600;700;800&family=Quicksand:wght@400;500&display=swap">
<style>
  :root {
    --stage: #f2f3f5;
    --cover: #62acd6;
    --ink: #1b1b1b;
    --light: #e9ebec;
  }
  * { box-sizing: border-box; margin: 0; padding: 0; }
  html, body {
    width: 1200px;
    height: 857px;
    overflow: hidden;
    background: var(--stage);
  }
  .cover {
    position: absolute;
    left: 210px;
    top: 38px;
    width: 780px;
    height: 780px;
    background: var(--cover);
    display: flex;
    flex-direction: column;
    align-items: center;
  }
  .title {
    margin-top: 140px;
    display: flex;
    flex-direction: column;
    align-items: center;
    font-family: "Montserrat", sans-serif;
    line-height: 1;
  }
  .title-lines {
    display: flex;
    flex-direction: column;
    align-items: flex-start;
  }
  .title-top {
    margin-left: 40px;
    font-size: 72px;
    font-weight: 800;
    color: var(--ink);
    letter-spacing: 0.01em;
  }
  .title-middle {
    margin-top: 8px;
    font-size: 86px;
    font-weight: 600;
    color: var(--light);
    letter-spacing: 0.02em;
  }
  .title-box {
    margin-top: 30px;
    padding: 10px 30px 12px;
    border: 3px solid var(--light);
    font-size: 56px;
    font-weight: 800;
    color: var(--ink);
    letter-spacing: 0.04em;
  }
  .subtitle {
    margin-top: 46px;
    font-family: "Quicksand", sans-serif;
    font-weight: 500;
    font-size: 29px;
    line-height: 1.2;
    color: var(--ink);
    text-align: center;
  }
  .author {
    margin-top: 74px;
    font-family: "Montserrat", sans-serif;
    font-weight: 800;
    font-size: 42px;
    letter-spacing: 0.09em;
    color: var(--ink);
  }
</style>
</head>
<body>
  <main class="cover">
    <h1 class="title">
      <span class="title-lines">
        <span class="title-top">BRIGHT</span>
        <span class="title-middle">MAKERS</span>
      </span>
      <span class="title-box">MANUAL</span>
    </h1>
    <p class="subtitle">55 ways to build products and<br>services people want</p>
    <p class="author">MARIEKE VOLLEN</p>
  </main>
</body>
</html>
```